Signage Design Project

We are a company that sells roses at university and college graduations. We are looking for a sign for conferences. The sign will be a long lengthwise sign, 33.5w x 80xh
It doesn't need to be overwhelmingly flashy, it just needs to get our message across. We will require two signs, one with the "Marlowe Blooms" logo, and a second with the "Fenwick Petal Co." logo. These logos are uploaded in both PNG and JPEG formats. The alternative option is to create one image with both logos, but we would much prefer two separate ones. We will NOT look at anything overly flashy. Ideally we need a simple, aesthetically pleasing graphic that will look good on a vertical pop up stand.

Industry/Entity Type

University

Requirements
Must have
• Our logo (Marlowe Blooms for one, Fenwick Petal Co. for the other)

```html
<!DOCTYPE html>
<html lang="en">
<head>
<meta charset="utf-8">
<title>Graduation Flower Pop-up Banners</title>
<link rel="stylesheet" href="https://fonts.googleapis.com/css2?family=Roboto+Condensed:wght@700&family=Open+Sans:ital,wght@1,600&display=swap">
<style>
  :root {
    --page-bg: #f3f3f3;
    --banner-bg: #ffffff;
    --banner-edge: #e2e2e2;
    --brand-green: #6a9a2c;
    --bloom-light: #e6e6e6;
    --bloom-mid: #d2d2d2;
  }
  * { box-sizing: border-box; margin: 0; padding: 0; }
  html, body {
    width: 1200px;
    height: 1059px;
    overflow: hidden;
    background: var(--page-bg);
  }
  .stage {
    position: relative;
    width: 1200px;
    height: 1059px;
    display: flex;
    justify-content: center;
    align-items: center;
    gap: 64px;
  }
  .banner {
    position: relative;
    width: 390px;
    height: 931px;
    background: var(--banner-bg);
    border: 1px solid var(--banner-edge);
    overflow: hidden;
  }
  .brand {
    position: absolute;
    top: 190px;
    right: 36px;
    text-align: right;
  }
  .brand-name {
    font-family: "Roboto Condensed", "Arial Narrow", sans-serif;
    font-weight: 700;
    font-size: 64px;
    line-height: 0.98;
    color: var(--brand-green);
    letter-spacing: -0.5px;
  }
  .tagline {
    margin-top: 14px;
    font-family: "Open Sans", Arial, sans-serif;
    font-style: italic;
    font-weight: 600;
    font-size: 21px;
    color: var(--brand-green);
  }
  .bloom-art {
    position: absolute;
    bottom: -40px;
    width: 420px;
    height: 470px;
    border-radius: 48% 48% 8% 8% / 55% 55% 10% 10%;
    background: radial-gradient(ellipse at 50% 45%, var(--bloom-mid) 0%, var(--bloom-light) 60%, rgba(230,230,230,0) 100%);
  }
  .banner--fenwick .bloom-art { right: -110px; }
  .banner--marlowe .bloom-art { left: -110px; }
</style>
</head>
<body>
  <main class="stage">
    <section class="banner banner--fenwick">
      <div class="brand">
        <p class="brand-name">Fenwick<br>Petal Co.</p>
        <p class="tagline">Flowers For Your Graduate</p>
      </div>
      <div class="bloom-art" role="img" aria-label="Large faint grey line illustration of a blooming flower"></div>
    </section>

    <section class="banner banner--marlowe">
      <div class="brand">
        <p class="brand-name">Marlowe<br>Blooms</p>
      </div>
      <div class="bloom-art" role="img" aria-label="Large faint grey line illustration of a blooming flower"></div>
    </section>
  </main>
</body>
</html>
```